Wren Vehicle Polishing (Mobile detail)

I need a business card made up. I'd like it to be different in some form, either raised, embossed, debossed, something cool that stands out. (preferably embossed text somewhere in it). I will be including the Initial png file. Let me know if you need the photoshop of adobe illustrator file to work with.

Information to be included: Text: XXX-XXX-XXXX Phone: XXX-XXX-XXXX Email: wrenpolishcrew@mailbox-demo.net Website: www.socialpage-demo.net/wrenpolishKTR Hours of operation: Mon - Fri 7:00AM to 8:00PM Sat - 10:00AM to 8:00PM

Target Market(s)

Mobile automotive detailing

Industry/Entity Type

Automotive

Contact Information for Business Card

Make it stand out with embossed lettering, I'd also like the background to be glossy black or matte, something that represents a shiny car, black preferred

Requirements
Must have
• A glossy background, or something.
• My logo, pick one of them that best fits your design.
Should not have
• White background,
• something that does not stand out.

```html
<!DOCTYPE html>
<html lang="en">
<head>
<meta charset="UTF-8">
<title>Wren Vehicle Polishing — Business Card</title>
<link rel="stylesheet" href="https://fonts.googleapis.com/css2?family=Lora:ital,wght@1,700&family=Open+Sans:wght@400;700&display=swap">
<style>
  :root {
    --backdrop: #2e2927;
    --card-black: #1c1c1e;
    --card-black-hi: #2a2a2d;
    --accent-orange: #ff6a00;
    --silver: #d4d6d9;
    --silver-dark: #8c8f93;
    --text-white: #f4f4f4;
  }
  * { margin: 0; padding: 0; box-sizing: border-box; }
  html, body {
    width: 1200px;
    height: 716px;
    overflow: hidden;
  }
  body {
    background: var(--backdrop);
    font-family: "Open Sans", Arial, sans-serif;
    position: relative;
  }
  .card {
    position: absolute;
    top: 215px;
    width: 500px;
    height: 286px;
    border-radius: 4px;
    background: radial-gradient(ellipse at 35% 30%, var(--card-black-hi) 0%, var(--card-black) 70%);
    box-shadow: 0 10px 24px rgba(0,0,0,0.45);
    overflow: hidden;
  }
  .card--front { left: 70px; }
  .card--back { left: 630px; }

  .brand-mark {
    position: absolute;
    display: flex;
    align-items: center;
    gap: 10px;
  }
  .brand-mark__dot {
    width: 22px;
    height: 22px;
    border-radius: 50%;
    background: var(--accent-orange);
    flex-shrink: 0;
  }
  .brand-mark__name {
    font-family: "Open Sans", Arial, sans-serif;
    font-weight: 700;
    color: var(--silver);
    line-height: 1.1;
  }
  .card--front .brand-mark {
    left: 50%;
    top: 50%;
    transform: translate(-50%, -50%);
  }
  .card--front .brand-mark__name { font-size: 26px; }
  .card--back .brand-mark {
    left: 318px;
    top: 132px;
    width: 165px;
  }
  .card--back .brand-mark__name { font-size: 17px; }

  .accent-band {
    position: absolute;
    left: 0;
    top: 0;
    width: 36px;
    height: 100%;
    background: var(--accent-orange);
  }
  .accent-rule {
    position: absolute;
    left: 36px;
    top: 0;
    width: 5px;
    height: 100%;
    background: linear-gradient(90deg, var(--silver-dark), var(--silver), var(--silver-dark));
  }

  .holder-name {
    position: absolute;
    left: 78px;
    top: 40px;
    font-family: "Lora", Georgia, serif;
    font-style: italic;
    font-weight: 700;
    font-size: 19px;
    color: var(--text-white);
  }
  .contact-list {
    position: absolute;
    left: 62px;
    top: 112px;
    list-style: none;
  }
  .contact-list li {
    display: flex;
    align-items: center;
    gap: 10px;
    font-size: 12.5px;
    color: var(--text-white);
    height: 19px;
  }
  .contact-icon {
    width: 11px;
    height: 11px;
    flex-shrink: 0;
  }
  .hours {
    position: absolute;
    left: 62px;
    top: 176px;
    font-size: 12.5px;
    line-height: 19px;
    color: var(--text-white);
  }
  .hours__label { color: var(--accent-orange); }
</style>
</head>
<body>

  <section class="card card--front" aria-label="Business card front">
    <div class="brand-mark">
      <span class="brand-mark__dot"></span>
      <span class="brand-mark__name">Wren Vehicle Polishing</span>
    </div>
  </section>

  <section class="card card--back" aria-label="Business card back">
    <div class="accent-band"></div>
    <div class="accent-rule"></div>

    <h1 class="holder-name">Your Name</h1>

    <ul class="contact-list">
      <li>
        <svg class="contact-icon" viewBox="0 0 12 12" aria-hidden="true">
          <rect width="12" height="12" rx="2" fill="var(--accent-orange)"/>
          <path d="M3 3.5 Q6 2 9 3.5 L8.2 5 L7 4.6 L7 5.6 L5 5.6 L5 4.6 L3.8 5 Z M4 6.5 H8 V9 H4 Z" fill="#1c1c1e"/>
        </svg>
        <span>XXX-XXX-XXXX</span>
      </li>
      <li>
        <svg class="contact-icon" viewBox="0 0 12 12" aria-hidden="true">
          <rect width="12" height="12" rx="2" fill="var(--accent-orange)"/>
          <rect x="2.5" y="3.5" width="7" height="5" fill="none" stroke="#1c1c1e" stroke-width="1"/>
          <path d="M2.5 3.5 L6 6.3 L9.5 3.5" fill="none" stroke="#1c1c1e" stroke-width="1"/>
        </svg>
        <span>wrenpolishcrew@mailbox-demo.net</span>
      </li>
      <li>
        <svg class="contact-icon" viewBox="0 0 12 12" aria-hidden="true">
          <rect width="12" height="12" rx="2" fill="var(--accent-orange)"/>
        </svg>
        <span>/wrenpolishKTR</span>
      </li>
    </ul>

    <p class="hours">
      <span class="hours__label">Hours of operation:</span><br>
      Mon - Fri 7:00AM to 8:00PM<br>
      Sat - 10:00AM to 8:00PM
    </p>

    <div class="brand-mark">
      <span class="brand-mark__dot"></span>
      <span class="brand-mark__name">Wren Vehicle Polishing</span>
    </div>
  </section>

</body>
</html>
```